Retirement Plan Advisor Bio

See the attached document and photo for content. I would like someone to design this one page flyer using my logo. This logo was designed by a designer with craft nest. I am looking for a professional looking document. I want to he color scheme to be primarily white and gold.

Target Market(s)

Employers who offer a retirement plan

Requirements
Should not have
• The designs that I have received look more like resumes. I am interested in advertising my Retirement plan services. If anyone can change their submissions and change it to an ad for retirement plan services instead of a Bio or resume, I would prefer that.

```html
<!DOCTYPE html>
<html lang="en">
<head>
<meta charset="utf-8">
<title>Retirement Plan Advisor – Helen R Talbot</title>
<link href="https://fonts.googleapis.com/css2?family=Montserrat:wght@300;400;500&family=Arimo:wght@400;700&display=swap" rel="stylesheet">
<style>
  :root {
    --backdrop: #e4dbd1;
    --paper: #ffffff;
    --panel: #efeeed;
    --charcoal: #262a28;
    --gold: #b89a5e;
    --gold-light: #c9ad73;
    --brown: #6e3b1c;
    --rule: #d9c9b0;
    --ink: #333333;
  }
  * { box-sizing: border-box; margin: 0; padding: 0; }
  html, body { width: 1199px; height: 1200px; overflow: hidden; }
  body { background: var(--backdrop); position: relative; font-family: "Arimo", Arial, sans-serif; color: var(--ink); }

  .flyer { position: absolute; left: 220px; top: 62px; width: 760px; height: 1075px; background: var(--paper); overflow: hidden; box-shadow: 0 10px 30px rgba(80,60,40,.18); }

  .sidebar { position: absolute; left: 0; top: 110px; width: 290px; height: 710px; background: var(--charcoal); }
  .portrait { position: absolute; left: 0; top: 0; width: 290px; height: 360px;
    background: linear-gradient(180deg, #3d5a7e 0%, #4f5f8a 40%, #3b4048 80%, var(--charcoal) 100%); }
  .gold-band { position: absolute; left: 0; top: 820px; width: 290px; height: 62px; background: var(--gold); }

  .identity { position: absolute; left: 0; top: 420px; width: 290px; text-align: center; }
  .identity .name { font-family: "Montserrat", sans-serif; font-weight: 300; font-size: 21px; color: var(--gold-light); }
  .identity .role { font-family: "Montserrat", sans-serif; font-weight: 300; font-size: 14px; color: #d8d3c8; margin-top: 4px; }

  .contact { position: absolute; left: 40px; top: 520px; list-style: none; }
  .contact li { display: flex; align-items: flex-start; gap: 14px; font-size: 13px; color: #e2ddd3; margin-bottom: 14px; line-height: 1.45; }
  .contact svg { flex: none; width: 20px; height: 20px; stroke: var(--gold); fill: none; stroke-width: 1.4; }
  .contact-underline { position: absolute; left: 40px; top: 740px; width: 190px; height: 2px; background: #e8dcc4; }

  .content-panel { position: absolute; left: 290px; top: 480px; width: 470px; height: 450px; background: var(--panel); }
  .edge-rule { position: absolute; right: 14px; top: 110px; width: 5px; height: 690px; background: var(--gold); }
  .edge-accent { position: absolute; right: 14px; top: 760px; width: 5px; height: 70px; background: var(--brown); }

  .section { position: absolute; left: 330px; width: 380px; }
  .section h2 { font-family: "Montserrat", sans-serif; font-weight: 500; font-size: 14px; letter-spacing: 4px; color: var(--gold); padding-bottom: 6px; border-bottom: 1px solid var(--rule); margin-bottom: 14px; }
  .section .body { border-left: 1px solid #a9764f; padding-left: 12px; font-size: 13px; line-height: 1.6; }
  .section ul { list-style: none; }
  .section li::before { content: "» "; font-size: 10px; }
  .about { top: 130px; }
  .specialties { top: 300px; }
  .qualifications { top: 535px; }
  .education { top: 740px; }
  .education strong { font-size: 14px; }

  .footer-brand { position: absolute; left: 0; top: 960px; width: 760px; height: 80px; }
  .footer-brand .lines { position: absolute; top: 38px; height: 6px; border-top: 1.5px solid var(--gold); border-bottom: 1.5px solid var(--gold); }
  .footer-brand .lines.left { left: 40px; width: 220px; }
  .footer-brand .lines.right { right: 40px; width: 220px; }
  .brand-name { position: absolute; left: 270px; top: 28px; width: 220px; display: flex; align-items: center; justify-content: center; gap: 8px; font-family: "Montserrat", sans-serif; font-weight: 500; font-size: 17px; color: var(--gold); white-space: nowrap; }
  .brand-name .mark { width: 14px; height: 14px; background: var(--gold); }
</style>
</head>
<body>
  <main class="flyer">
    <aside class="sidebar">
      <div class="portrait" role="img" aria-label="Portrait photo of the advisor"></div>
      <div class="identity">
        <p class="name">Helen R Talbot CPC RFA</p>
        <p class="role">Keystone Wealth Advisor</p>
      </div>
      <ul class="contact">
        <li><svg viewBox="0 0 20 20"><rect x="2" y="5" width="16" height="11"/><path d="M2 5l8 6 8-6"/></svg>helen.talbot@keystonewealth.com</li>
        <li><svg viewBox="0 0 20 20"><path d="M5 2l3 4-2 2c1 2 3 4 5 5l2-2 4 3-2 3C9 17 3 11 2 5z"/></svg>(555)014.2290</li>
        <li><svg viewBox="0 0 20 20"><path d="M10 18s6-6 6-10a6 6 0 0 0-12 0c0 4 6 10 6 10z"/><circle cx="10" cy="8" r="2"/></svg>240 Meridian Ave.<br>Fairview, WM 00000</li>
        <li><svg viewBox="0 0 20 20"><circle cx="10" cy="10" r="8"/><path d="M2 10h16M10 2c3 3 3 13 0 16M10 2c-3 3-3 13 0 16"/></svg>www.helentalbot.com</li>
      </ul>
      <div class="contact-underline"></div>
    </aside>
    <div class="gold-band"></div>

    <div class="content-panel"></div>
    <div class="edge-rule"></div>
    <div class="edge-accent"></div>

    <section class="section about">
      <h2>ABOUT ME</h2>
      <p class="body">I strive to improve retirement outcomes for my plan sponsor clients and their employees through careful retirement plan design assistance, strategic and targeted communication and education, as well as continual monitoring of results.</p>
    </section>

    <section class="section specialties">
      <h2>PROFESSIONAL SPECIALTIES</h2>
      <ul class="body">
        <li>Over 15 years of experience in the retirement plan industry</li>
        <li>Focused on helping plan sponsors reduce administrative burdens and fiduciary risk</li>
        <li>Dedicated to helping employees work toward a positive retirement outcome through careful analysis of their savings rate, investment strategy and overall financial wellness</li>
      </ul>
    </section>

    <section class="section qualifications">
      <h2>QUALIFICATIONS</h2>
      <ul class="body">
        <li>Chartered Plan Consultant</li>
        <li>Registered Fiduciary Advisor</li>
        <li>Investment Advisor Representative</li>
        <li>Series A, B, and C Securities licenses with Keystone Wealth</li>
        <li>Holds Life and Health Insurance licenses from the state of Westmark</li>
      </ul>
    </section>

    <section class="section education">
      <h2>EDUCATION</h2>
      <div class="body">
        <strong>BS Brookfield University, 1994</strong>
        <p>*Securities and Investment Advisory Services offered through Keystone Wealth Holdings, Inc, a Registered Broker/Dealer and Investment Advisor, member FSRA/ISPC</p>
      </div>
    </section>

    <footer class="footer-brand">
      <div class="lines left"></div>
      <div class="brand-name"><span class="mark"></span>Harborline Partners</div>
      <div class="lines right"></div>
    </footer>
  </main>
</body>
</html>
```